Brindle Logistics Business Card Design

We are a trucking and warehousing company. We run freight in the US manly from the Pacific NW to TX and back up the the PNW. We also do warehousing where we store, move, and distribute freight. Looking for a clean and modern design of business card. We would like to look rich and elegant. Attached is our logo.

Industry/Entity Type

Trucking Company

Contact Information for Business Card

Looking for a clean and modern design of business card. We would like to look rich and elegant.

Font styles to use
Sans Serif

Colors

Designer to choose colors to be used in the design.

Requirements
Must have
• logo but it should not dominate the card
Should not have
• logo should not dominate the card

```html
<!DOCTYPE html>
<html lang="en">
<head>
<meta charset="utf-8">
<title>Brindle Logistics Business Card</title>
<link rel="stylesheet" href="https://fonts.googleapis.com/css2?family=Lato:wght@400;700&family=Libre+Baskerville:wght@700&display=swap">
<style>
  :root {
    --bg-top: #9aa2b3;
    --bg-bottom: #ecebeb;
    --paper: #f7f7f7;
    --brand-blue: #1c6fc4;
    --deep-blue: #0f5fae;
    --light-blue: #3d98d8;
    --ink: #2b2220;
    --muted-line: #d9d9d9;
    --white: #ffffff;
  }
  * { box-sizing: border-box; margin: 0; padding: 0; }
  html, body { width: 1200px; height: 768px; overflow: hidden; }
  body {
    background: linear-gradient(180deg, var(--bg-top) 0%, var(--bg-bottom) 100%);
    font-family: "Lato", sans-serif;
    position: relative;
  }
  .card {
    position: absolute;
    width: 490px;
    height: 280px;
    top: 244px;
    overflow: hidden;
    box-shadow: 0 14px 30px rgba(40, 50, 70, 0.25);
  }
  /* Front side */
  .card-front { left: 70px; background: var(--paper); }
  .card-front .swoosh { position: absolute; inset: 0; width: 100%; height: 100%; }
  .card-front .brand {
    position: absolute;
    left: 34px;
    top: 120px;
    width: 190px;
    display: flex;
    align-items: center;
    gap: 8px;
  }
  .brand-dot {
    width: 16px; height: 16px; border-radius: 50%;
    background: var(--brand-blue);
    flex: none;
  }
  .brand-name {
    font-weight: 700;
    font-size: 17px;
    line-height: 1.1;
    color: var(--brand-blue);
    letter-spacing: 0.5px;
  }
  .divider {
    position: absolute;
    left: 240px;
    top: 0;
    width: 1px;
    height: 250px;
    background: var(--muted-line);
  }
  .contact {
    position: absolute;
    left: 262px;
    top: 58px;
  }
  .person-name {
    font-family: "Libre Baskerville", serif;
    font-weight: 700;
    font-size: 17px;
    color: var(--ink);
  }
  .person-title {
    font-size: 13px;
    color: var(--ink);
    margin: 2px 0 10px;
  }
  .contact-list { list-style: none; }
  .contact-item {
    display: flex;
    align-items: center;
    gap: 8px;
    font-size: 12.5px;
    color: var(--brand-blue);
    margin-bottom: 5px;
  }
  .contact-icon {
    width: 14px; height: 14px; border-radius: 50%;
    background: var(--brand-blue);
    display: flex; align-items: center; justify-content: center;
    flex: none;
  }
  .contact-icon svg { width: 9px; height: 9px; }
  /* Back side */
  .card-back {
    left: 640px;
    background: radial-gradient(circle at 35% 60%, var(--light-blue) 0%, var(--brand-blue) 45%, var(--deep-blue) 100%);
    display: flex;
    align-items: center;
    justify-content: center;
  }
  .card-back .brand { display: flex; align-items: center; gap: 10px; }
  .card-back .brand-dot { width: 22px; height: 22px; background: var(--white); }
  .card-back .brand-name { font-size: 26px; color: var(--white); }
</style>
</head>
<body>
  <section class="card card-front" aria-label="Business card front">
    <svg class="swoosh" viewBox="0 0 490 280" preserveAspectRatio="none" aria-hidden="true">
      <path d="M0 280 C 180 262, 380 200, 490 95 L 490 280 Z" fill="var(--brand-blue)"/>
      <path d="M0 280 C 190 255, 390 190, 490 110 L 490 125 C 390 205, 200 268, 20 280 Z" fill="var(--light-blue)" opacity="0.6"/>
    </svg>
    <div class="brand">
      <span class="brand-dot"></span>
      <span class="brand-name">Brindle Logistics, LLC</span>
    </div>
    <div class="divider"></div>
    <div class="contact">
      <p class="person-name">Your Name</p>
      <p class="person-title">Title</p>
      <ul class="contact-list">
        <li class="contact-item">
          <span class="contact-icon"><svg viewBox="0 0 10 10"><path d="M2 1 L4 3 L3 4 C3.5 5.5 4.5 6.5 6 7 L7 6 L9 8 L8 9 C4 9 1 6 1 2 Z" fill="var(--white)"/></svg></span>
          (000) 000-0000
        </li>
        <li class="contact-item">
          <span class="contact-icon"><svg viewBox="0 0 10 10"><rect x="1" y="2.5" width="8" height="5" fill="none" stroke="var(--white)" stroke-width="1"/><path d="M1 2.5 L5 5.5 L9 2.5" fill="none" stroke="var(--white)" stroke-width="1"/></svg></span>
          abc@brindlelogistics.com
        </li>
        <li class="contact-item">
          <span class="contact-icon"><svg viewBox="0 0 10 10"><path d="M5 9.5 C3 7 2 5.5 2 4 A3 3 0 0 1 8 4 C8 5.5 7 7 5 9.5 Z" fill="var(--white)"/><circle cx="5" cy="4" r="1.1" fill="var(--brand-blue)"/></svg></span>
          your office address
        </li>
      </ul>
    </div>
  </section>

  <section class="card card-back" aria-label="Business card back">
    <div class="brand">
      <span class="brand-dot"></span>
      <span class="brand-name">Brindle Logistics, LLC</span>
    </div>
  </section>
</body>
</html>
```